Halden & Pruitt Periodontics and Implant Solutions Business Card

We are a specialty dental practice- implants and periodontal surgery. We have just re-designed our logo and are building a new office and would like to re-design our business card. We are looking for something professional with a creative and artsy twist- something to stand out among the rest! Happy Designing!

I have uploaded all versions of our new logo and our current business card. We have 3 locations and 2 doctors.

Target Market(s)

55+

Industry/Entity Type

Dental

Contact Information for Business Card

Needs Names, logo, locations- professional and artsy!

Colors
0555a3
0592cd
34a7d7
3277b5
85cae6
85acd3
cee9f5
ecf7fb

Requirements
Must have
• our names:
• Thomas E. Halden D.M.D.
• Celia M. Pruitt D.M.D.
• Diplomate of the National Council of Gum Surgery
• Address locations:
• 462 W. Larkspur Avenue Suite 210B Plantation, FL 33871
• Tel: 954-318-2264 Fax: 954-318-2291
• 5127 Harlow Lane #C-4 Boca Raton, FL 33609
• Tel: 561-627-1958 Fax: 561-703-2816
• 274 Northwest 9th Street #412 Miami FL 33987
• Tel: 786-429-6153 Fax: 786-429-6170
Nice to have
• unique look
Should not have
• doesn't need QR like our current card has.

```html
<!DOCTYPE html>
<html lang="en">
<head>
<meta charset="utf-8">
<title>Halden &amp; Pruitt Periodontics and Implant Solutions – Business Card</title>
<link rel="stylesheet" href="https://fonts.googleapis.com/css2?family=Source+Sans+3:wght@400;600&display=swap">
<style>
  :root {
    --stage: #2b2b2d;
    --card: #0b0b0d;
    --ink: #f2f2f2;
    --brand-blue: #3158b0;
    --icon-blue: #3a63c4;
    --rule: #1f2f5a;
  }
  * { box-sizing: border-box; margin: 0; padding: 0; }
  html, body { width: 1200px; height: 900px; overflow: hidden; }
  body {
    background: var(--stage);
    font-family: "Source Sans 3", "Myriad Pro", Arial, sans-serif;
    color: var(--ink);
    position: relative;
  }
  .card {
    position: absolute;
    top: 290px;
    width: 540px;
    height: 320px;
    background: var(--card);
    border-radius: 22px;
  }
  .card--front { left: 45px; }
  .card--back { left: 615px; }

  .brand {
    position: absolute;
    display: flex;
    flex-direction: column;
    align-items: center;
    text-align: center;
    color: var(--ink);
    font-weight: 400;
  }
  .brand__ring {
    width: 120px; height: 120px;
    border: 5px solid var(--ink);
    border-radius: 50%;
    margin-bottom: 12px;
  }
  .brand__name { font-size: 15px; line-height: 1.25; }
  .card--front .brand { left: 22px; top: 70px; width: 200px; }
  .card--back .brand { left: 26px; top: 76px; width: 180px; }

  .divider {
    position: absolute;
    left: 240px; top: 38px;
    width: 1px; height: 244px;
    background: var(--rule);
  }
  .doctors {
    position: absolute;
    left: 264px; top: 52px;
  }
  .doctors__name {
    color: var(--brand-blue);
    font-weight: 600;
    font-size: 22px;
    line-height: 1.12;
  }
  .doctors__title {
    font-size: 17px;
    line-height: 1.25;
    margin-top: 6px;
  }
  .contact {
    position: absolute;
    left: 264px; top: 208px;
    list-style: none;
    font-size: 17px;
    line-height: 1.5;
  }
  .contact li, .office__line { display: flex; align-items: center; gap: 8px; }
  .icon { width: 13px; height: 13px; fill: var(--icon-blue); flex: none; }

  .offices {
    position: absolute;
    left: 222px; top: 30px;
    list-style: none;
    font-size: 14px;
    line-height: 1.3;
  }
  .office { margin-bottom: 18px; }
  .office__address { display: flex; gap: 8px; }
  .office__address .icon { margin-top: 2px; }
  .office__numbers { display: flex; gap: 22px; margin-top: 2px; padding-left: 0; }
</style>
</head>
<body>
  <svg width="0" height="0" style="position:absolute" aria-hidden="true">
    <defs>
      <symbol id="i-pin" viewBox="0 0 12 16"><path d="M6 0a6 6 0 0 0-6 6c0 4.5 6 10 6 10s6-5.5 6-10a6 6 0 0 0-6-6zm0 8.5A2.5 2.5 0 1 1 6 3.5a2.5 2.5 0 0 1 0 5z"/></symbol>
      <symbol id="i-phone" viewBox="0 0 16 16"><path d="M3.6 1l2.3 3.2-1.4 1.6c.9 2 2.6 3.8 4.7 4.7l1.6-1.4L14 11.4 13.1 14C7 14 2 9 2 2.9z"/></symbol>
      <symbol id="i-fax" viewBox="0 0 16 16"><path d="M4 1h7v4H4zM1 6h14v8H1zm3 3v3h8V9z"/></symbol>
      <symbol id="i-mail" viewBox="0 0 16 12"><path d="M0 0h16v12H0zm1.5 1.5L8 6.5l6.5-5z"/></symbol>
      <symbol id="i-web" viewBox="0 0 16 16"><path d="M8 0a8 8 0 1 0 0 16A8 8 0 0 0 8 0zm5.9 7h-2.8a12 12 0 0 0-1.3-5 6 6 0 0 1 4.1 5zM8 2c.9 1.2 1.5 3 1.6 5H6.4C6.5 5 7.1 3.2 8 2zM6.2 2a12 12 0 0 0-1.3 5H2.1a6 6 0 0 1 4.1-5zM2.1 9h2.8a12 12 0 0 0 1.3 5 6 6 0 0 1-4.1-5zM8 14c-.9-1.2-1.5-3-1.6-5h3.2c-.1 2-.7 3.8-1.6 5zm1.8 0a12 12 0 0 0 1.3-5h2.8a6 6 0 0 1-4.1 5z"/></symbol>
    </defs>
  </svg>

  <section class="card card--front" aria-label="Business card front">
    <div class="brand">
      <div class="brand__ring"></div>
      <p class="brand__name">Halden &amp; Pruitt<br>Periodontics and Implant Solutions</p>
    </div>
    <div class="divider"></div>
    <div class="doctors">
      <p class="doctors__name">Thomas E. Halden D.M.D.</p>
      <p class="doctors__name">Celia M. Pruitt D.M.D.</p>
      <p class="doctors__title">Diplomate of the National<br>Council of Gum Surgery</p>
    </div>
    <ul class="contact">
      <li><svg class="icon"><use href="#i-mail"/></svg>contactus@haldenperio.com</li>
      <li><svg class="icon"><use href="#i-web"/></svg>www.haldenperio.com</li>
    </ul>
  </section>

  <section class="card card--back" aria-label="Business card back">
    <div class="brand">
      <div class="brand__ring"></div>
      <p class="brand__name">Halden &amp; Pruitt<br>Periodontics and Implant Solutions</p>
    </div>
    <ul class="offices">
      <li class="office">
        <div class="office__address"><svg class="icon"><use href="#i-pin"/></svg><span>462 W. Larkspur Avenue Suite<br>210B Plantation, FL 33871</span></div>
        <div class="office__numbers">
          <span class="office__line"><svg class="icon"><use href="#i-phone"/></svg>954-318-2264</span>
          <span class="office__line"><svg class="icon"><use href="#i-fax"/></svg>954-318-2291</span>
        </div>
      </li>
      <li class="office">
        <div class="office__address"><svg class="icon"><use href="#i-pin"/></svg><span>5127 Harlow Lane #C-4<br>Boca Raton, FL 33609</span></div>
        <div class="office__numbers">
          <span class="office__line"><svg class="icon"><use href="#i-phone"/></svg>561-627-1958</span>
          <span class="office__line"><svg class="icon"><use href="#i-fax"/></svg>561-703-2816</span>
        </div>
      </li>
      <li class="office">
        <div class="office__address"><svg class="icon"><use href="#i-pin"/></svg><span>274 Northwest 9th Street<br>#412 Miami FL 33987</span></div>
        <div class="office__numbers">
          <span class="office__line"><svg class="icon"><use href="#i-phone"/></svg>786-429-6153</span>
          <span class="office__line"><svg class="icon"><use href="#i-fax"/></svg>786-429-6170</span>
        </div>
      </li>
    </ul>
  </section>
</body>
</html>
```